Electrician Business Card/ company logo/small business

New Business Cards and logo needed that will catch peoples eye and say we went that extra step. Attached is a design possibly to be incorporated, if u have your own great, lets see it!... This will be a small local business. thank you for all you do!
Falcon Electric
Dov Merrick Owner
Journeyman Electrician
phone 1.482.639.2075
email: QRTFalconElectric@zentromail.com
call for free estimate!
Updates

Accepted and approved for cards

Target Market(s)

support small local business

Industry/Entity Type

Electrical,

Contact Information for Business Card

name, title,company/ logo, phone, email, free estimate

Font styles to use
Other font styles liked:
• easy to read

Colors

Designer to choose colors to be used in the design.

Requirements
Must have
• eye catching everything! logo and falcon electric listed on business card/logo, incorp logo in the background of card
Nice to have
• lightening bolts in eyes or around the triangle? vertical, modern, any design that would be unique and stand out
Should not have
• pinks, reds, yellows,brown

```html
<!DOCTYPE html>
<html lang="en">
<head>
<meta charset="utf-8">
<title>Falcon Electric – Business Card</title>
<link href="https://fonts.googleapis.com/css2?family=Michroma&family=Exo+2:wght@600;700&family=Roboto:wght@500&display=swap" rel="stylesheet">
<style>
  :root {
    --backdrop: #6c8fc0;
    --card: #232425;
    --facet: rgba(255,255,255,0.025);
    --facet-dark: rgba(0,0,0,0.12);
    --green: #7aa83c;
    --lime: #8cc63f;
    --blue: #0a86c9;
    --white: #ffffff;
  }
  * { margin: 0; padding: 0; box-sizing: border-box; }
  html, body { width: 1200px; height: 1200px; overflow: hidden; }
  body { background: var(--backdrop); position: relative; }

  .card {
    position: absolute; left: 259px; top: 35px;
    width: 682px; height: 1130px;
    background: var(--card);
    overflow: hidden;
  }
  .card-facets { position: absolute; inset: 0; width: 100%; height: 100%; }

  .brand {
    position: absolute; left: 82px; top: 182px;
    display: flex; align-items: center; gap: 22px;
  }
  .brand-mark { width: 56px; height: 56px; background: var(--lime); }
  .brand-name {
    font-family: "Michroma", sans-serif; font-size: 40px;
    color: var(--lime); letter-spacing: 1px; white-space: nowrap;
  }

  .person-name {
    position: absolute; left: 72px; top: 558px;
    font-family: "Michroma", sans-serif; font-size: 54px;
    color: var(--white); letter-spacing: 1px; white-space: nowrap;
  }
  .person-role {
    position: absolute; left: 72px; top: 632px;
    font-family: "Roboto", sans-serif; font-weight: 500; font-size: 31px;
    color: var(--white); letter-spacing: -1px;
  }
  .divider {
    position: absolute; left: 75px; right: 0; top: 691px; height: 3px;
    background: linear-gradient(90deg, var(--green), var(--blue));
  }
  .trade {
    position: absolute; left: 72px; top: 714px;
    font-family: "Roboto", sans-serif; font-weight: 500; font-size: 34px;
    color: var(--green); white-space: nowrap;
  }

  .contact {
    position: absolute; left: 83px;
    display: flex; align-items: center; gap: 34px;
    font-family: "Exo 2", sans-serif; color: var(--white);
  }
  .contact-phone { top: 853px; font-size: 41px; font-weight: 700; letter-spacing: 1px; }
  .contact-email { top: 943px; font-size: 27px; font-weight: 600; }
  .contact-icon {
    width: 63px; height: 60px; flex: none;
    background: linear-gradient(135deg, var(--lime), var(--blue));
    display: flex; align-items: center; justify-content: center;
  }
  .contact-icon svg { width: 36px; height: 36px; }
</style>
</head>
<body>
  <div class="card">
    <svg class="card-facets" viewBox="0 0 682 1130" preserveAspectRatio="none" aria-hidden="true">
      <polygon points="0,0 682,0 682,120 300,60" fill="var(--facet)"/>
      <polygon points="0,90 420,380 0,470" fill="var(--facet-dark)"/>
      <polygon points="200,0 682,290 682,140" fill="var(--facet)"/>
      <polygon points="0,330 682,120 682,250 250,500" fill="var(--facet)"/>
      <polygon points="0,360 350,495 0,495" fill="var(--facet-dark)"/>
      <polygon points="348,495 682,350 682,495" fill="var(--blue)"/>
    </svg>

    <div class="brand">
      <span class="brand-mark"></span>
      <span class="brand-name">Falcon Electric</span>
    </div>

    <div class="person-name">DOV MERRICK</div>
    <div class="person-role">OWNER</div>
    <div class="divider"></div>
    <div class="trade">JOURNEYMAN ELECTRICIAN</div>

    <div class="contact contact-phone">
      <span class="contact-icon">
        <svg viewBox="0 0 24 24" fill="none" stroke="#fff" stroke-width="1.2" stroke-linejoin="round">
          <path d="M6.5 3.5l3 3-2 2.2c1 2.3 3.5 4.8 5.8 5.8l2.2-2 3 3-2.2 2.5C11 17.5 6.5 13 4 6.3z"/>
        </svg>
      </span>
      <span>1.482.639.2075</span>
    </div>

    <div class="contact contact-email">
      <span class="contact-icon">
        <svg viewBox="0 0 24 24" fill="none" stroke="#fff" stroke-width="1.2" stroke-linejoin="round">
          <rect x="3" y="6" width="18" height="12"/>
          <path d="M3 6l9 7 9-7M3 18l7-6M21 18l-7-6"/>
        </svg>
      </span>
      <span>qrtfalconelectric@zentromail.com</span>
    </div>
  </div>
</body>
</html>
```